Business Card Design for Venture Kite

Venture Kite is a pro bono student consultancy service offered by Corvala KTRB to social start ups and enterprises. We provide consulting services with expertise in areas such as Marketing, IT, Business Strategy and Innovation.
I have attached\ the Venture Kite Logo here for your perusal.
Industry/Entity Type
Business
Contact Information for Business Card
Name: Ha Min Park Name: Thomas Leung
Role: Project Leader Role: Vice Project Leader
M:0477203941 M: 0479352806
E: ha-min.park@corvalaktrb.org E: thomas.leung@corvalaktrb.org
W: www.corvalaktrb.org W: www.corvalaktrb.org

```html
<!DOCTYPE html>
<html lang="en">
<head>
<meta charset="utf-8">
<title>Venture Kite – Ha Min Park Business Card</title>
<link rel="stylesheet" href="https://fonts.googleapis.com/css2?family=Bebas+Neue&family=Montserrat:wght@500&display=swap">
<style>
  :root {
    --paper: #ffffff;
    --brand-orange: #f47216;
    --shadow-grey: #bdbdbd;
    --ink: #1b1b1b;
    --on-orange: #ffffff;
  }
  html, body {
    margin: 0;
    padding: 0;
    overflow: hidden;
    background: var(--paper);
  }
  .card {
    position: relative;
    width: 1200px;
    height: 742px;
    background: var(--paper);
    overflow: hidden;
  }
  .card__art {
    position: absolute;
    inset: 0;
    width: 1200px;
    height: 742px;
  }
  .shape-shadow { fill: var(--shadow-grey); }
  .shape-main { fill: var(--brand-orange); }
  .accent-lines line {
    stroke: var(--brand-orange);
    stroke-width: 1.3;
  }
  .plus-mark { fill: var(--on-orange); }

  .brand-name {
    position: absolute;
    left: 90px;
    top: 100px;
    margin: 0;
    font-family: "Bebas Neue", sans-serif;
    font-weight: 400;
    font-size: 72px;
    line-height: 0.95;
    letter-spacing: 1px;
    color: var(--ink);
  }
  .person {
    position: absolute;
    left: 738px;
    top: 150px;
    margin: 0;
    color: var(--on-orange);
    font-family: "Bebas Neue", sans-serif;
  }
  .person__name {
    margin: 0;
    font-size: 74px;
    font-weight: 400;
    line-height: 1;
    letter-spacing: 0.5px;
  }
  .person__role {
    margin: 10px 0 0;
    font-size: 36px;
    line-height: 1;
    letter-spacing: 0.5px;
  }
  .contact {
    position: absolute;
    left: 426px;
    top: 414px;
    margin: 0;
    padding: 0;
    list-style: none;
    font-family: "Montserrat", sans-serif;
    font-weight: 500;
    font-size: 27px;
    letter-spacing: 1.5px;
    text-transform: uppercase;
    color: var(--on-orange);
  }
  .contact__item {
    line-height: 57px;
    white-space: nowrap;
  }
</style>
</head>
<body>
  <div class="card">
    <svg class="card__art" viewBox="0 0 555 343" preserveAspectRatio="none" aria-hidden="true">
      <path class="shape-shadow" d="M348 16 L518 16 Q546 16 546 44 L546 214 Q546 240 520 240 L420 240 L410 256 L240 262 C195 264 160 285 150 312 L150 160 Q150 130 180 130 L285 130 C298 130 300 118 300 105 L300 46 Q300 16 348 16 Z"/>
      <path class="shape-main" d="M352 45 L503 45 Q530 45 530 72 L530 222 Q530 248 504 248 L432 248 L432 260 Q432 272 416 273 L250 280 C205 283 184 305 178 343 L178 182 Q178 150 210 150 L300 150 C314 150 318 140 318 125 L318 78 Q318 45 352 45 Z"/>
      <g class="accent-lines">
        <line x1="520" y1="58" x2="555" y2="24"/>
        <line x1="528" y1="78" x2="555" y2="52"/>
        <line x1="528" y1="102" x2="555" y2="76"/>
        <line x1="528" y1="126" x2="555" y2="100"/>
        <line x1="528" y1="150" x2="555" y2="124"/>
        <line x1="528" y1="174" x2="555" y2="148"/>
        <line x1="528" y1="198" x2="555" y2="172"/>
        <line x1="522" y1="228" x2="555" y2="196"/>
      </g>
      <g class="plus-mark">
        <rect x="324" y="161" width="36" height="8"/>
        <rect x="338" y="147" width="8" height="36"/>
      </g>
    </svg>

    <p class="brand-name">Venture<br>Kite</p>

    <div class="person">
      <h1 class="person__name">Ha Min Park</h1>
      <p class="person__role">Project Leader</p>
    </div>

    <ul class="contact">
      <li class="contact__item">Tel.: +61 047 720 39 41</li>
      <li class="contact__item">ha-min.park@corvalaktrb.org</li>
      <li class="contact__item">www.corvalaktrb.org</li>
    </ul>
  </div>
</body>
</html>
```